Business Card & Logo Design Project

I am looking for a slick/simple design for a logo and business card, for a music Producer/Mixer/Engineer.

I'm based in Tokyo, Japan and I help my clients polish up their creation to major radio/TV status. My clients pay me for my taste, sense of balance expertise and creative direction/

Design should give impression of seal of quality, professionalism, and enthusiasm need some sort of a logo like design for "vantiri productions".

Please don't include music notes or instruments or anything musically related and anything samurai or ninja or too much Japan in them on the design.

I like clever, slick stuff that's not too obvious.
I also like a smooth gradation type transition. My favorite color is deep dark blue/

Good Luck and Thank you for your effort.
Updates

I would like a two-sided design for this one.
One side with "vantiri productions" (all lower case) on, and the other side with my name and contact info.

Please also consider portrait position (or direction).  (as opposed to landscape) 

Target Market(s)

My primary targets are artists & bands, who want absolute best for their creation.

Industry/Entity Type

Business

Requirements
Must have
• Two-Sided
1, vantiri productions
2, Kenji Matsuda, Producer/Mixer/Engineer, +81 090 4827 3516, brightwaver@mailbox-example.com
Nice to have
• Any suggestions are welcome//
Should not have
• Anything music related images.
(e.g. CD, music notations, instruments etc.)

```html
<!DOCTYPE html>
<html lang="en">
<head>
<meta charset="utf-8">
<title>vantiri productions — business card</title>
<link href="https://fonts.googleapis.com/css2?family=Exo+2:wght@300;400;500&display=swap" rel="stylesheet">
<style>
  :root {
    --stage: #1c1c1e;
    --card-white: #f4f5f6;
    --card-navy: #1f3557;
    --card-navy-deep: #1a2d4a;
    --brand-blue: #1a6fc4;
    --bright-blue: #1d9ee3;
    --ghost-grey: #e6e7e9;
    --text-font: "Exo 2", sans-serif;
  }
  * { margin: 0; padding: 0; box-sizing: border-box; }
  html, body {
    width: 1200px; height: 900px; overflow: hidden;
    background: var(--stage);
    font-family: var(--text-font);
  }
  .canvas {
    position: relative; width: 1200px; height: 900px;
    display: flex; flex-direction: column; align-items: center; justify-content: center; gap: 56px;
  }
  .card {
    position: relative; width: 560px; height: 320px; overflow: hidden;
    box-shadow: 0 14px 30px rgba(0,0,0,.55);
  }
  /* Contact side */
  .card--contact { background: var(--card-white); }
  .ghost-name {
    position: absolute; left: 18px; bottom: 34px;
    font-size: 92px; font-weight: 500; line-height: .9;
    color: var(--ghost-grey); letter-spacing: -2px;
  }
  .contact-block {
    position: absolute; right: 34px; top: 34px; text-align: right;
  }
  .wordmark {
    font-size: 38px; font-weight: 500; color: var(--brand-blue);
    line-height: 1; letter-spacing: -.5px;
  }
  .person-name {
    margin-top: 22px; font-size: 19px; font-weight: 400; color: var(--brand-blue);
  }
  .person-role {
    margin-top: 4px; font-size: 14px; font-weight: 300; color: var(--brand-blue);
  }
  .contact-line {
    position: absolute; right: 34px; bottom: 30px;
    font-size: 13px; font-weight: 300; color: var(--brand-blue);
  }
  .contact-line .label { color: var(--bright-blue); margin-right: 4px; }
  .contact-line .item + .item { margin-left: 18px; }
  /* Brand side */
  .card--brand { background: var(--card-navy); }
  .brand-texture {
    position: absolute; inset: 0;
    background: linear-gradient(135deg, var(--card-navy) 0%, var(--card-navy-deep) 100%);
  }
  .brand-block {
    position: relative; height: 100%;
    display: flex; flex-direction: column; align-items: center; justify-content: center;
  }
  .brand-block .wordmark {
    font-size: 56px; color: var(--bright-blue);
  }
  .services {
    margin-top: 26px; font-size: 16px; font-weight: 300; letter-spacing: 2px;
    color: var(--bright-blue);
  }
  .services .divider { margin: 0 10px; }
</style>
</head>
<body>
<main class="canvas">
  <section class="card card--contact" aria-label="Contact side">
    <div class="ghost-name" aria-hidden="true">vantiri</div>
    <div class="contact-block">
      <div class="wordmark">vantiri productions</div>
      <div class="person-name">Kenji Matsuda</div>
      <div class="person-role">Producer/Mixer/Engineer</div>
    </div>
    <div class="contact-line">
      <span class="item"><span class="label">P:</span>+81 090 4827 3516</span>
      <span class="item"><span class="label">E:</span>brightwaver@mailbox-example.com</span>
    </div>
  </section>

  <section class="card card--brand" aria-label="Brand side">
    <div class="brand-texture" role="img" aria-label="Subtle repeating brand-name pattern on deep navy"></div>
    <div class="brand-block">
      <div class="wordmark">vantiri productions</div>
      <div class="services">Producer<span class="divider">|</span>Mixer<span class="divider">|</span>Engineer</div>
    </div>
  </section>
</main>
</body>
</html>
```